Property Management Company Website

I need a complete website for a property management company in Texas. Our current site (www.brindlehomesandleasing.com) needs to be revamped. My goal is to have a design that appeals more toward residential real estate investors rather than tenants. I would like the site to be more clean and business like. There is a lot of good content on the site that can be used; information about the company, services, etc. The main contact that focuses on real estate investors can be found on the investors and management tabs.

A sample site that I like can be found at: www.ferncrestpartnerstexas.com. I like it because it's clean, professional and easy to use. Hopefull this helps as a guide. I however, want this site to be unique.

I have NetPylon hosting services and also hearthway hosting services already set up.

I also want to make sure that we include links to our social media:
-Chirper - @brindlehomesnct
-Friendbook - www.facebook.com/brindlehomesandleasing
-ViewTube - www.youtube.com/BrindleHomesTX

Message me if you need any additional photos

Industry/Entity Type

Property Management

```html
<!DOCTYPE html>
<html lang="en">
<head>
<meta charset="utf-8">
<title>Brindle Homes and Leasing</title>
<link href="https://fonts.googleapis.com/css2?family=Kaushan+Script&family=Roboto:wght@300;400;500;700&display=swap" rel="stylesheet">
<style>
:root{
  --purple:#6a3b7d;
  --purple-dark:#5a2e6c;
  --gold:#c9962a;
  --text:#444;
  --muted:#666;
  --line:#d4d4d6;
  --grey-bg:#dedee0;
}
*{box-sizing:border-box;margin:0;padding:0}
html,body{width:1200px;height:1168px;overflow:hidden}
body{position:relative;font-family:"Roboto",Arial,sans-serif;color:var(--text);background:#fff}
.topbar{height:3px;background:var(--purple)}
.header{position:relative;height:55px;background:#fff;border-bottom:1px solid #e2e2e2}
.brand{position:absolute;left:183px;top:12px;font-size:28px;font-weight:500;color:var(--purple)}
.nav{position:absolute;left:316px;top:22px;display:flex;font-size:11px;letter-spacing:.4px}
.nav a{color:#444;text-decoration:none;text-transform:uppercase}
.nav span{margin:0 12px;color:#999}
.nav a.active{color:var(--purple);font-weight:700;text-decoration:underline}
.phone{position:absolute;left:819px;top:22px;font-size:10.5px;color:#444;display:flex;align-items:center;gap:5px}
.hero{position:relative;height:328px;background:#f1f1f1}
.hero-photo{position:absolute;left:440px;top:0;width:610px;height:328px;
  background:radial-gradient(ellipse at 55% 55%,#8a5a4c 0%,#7f8b6a 40%,#c6d4e6 65%,rgba(241,241,241,0) 80%)}
.tagline{position:absolute;left:180px;top:148px;width:215px;text-align:center;font-family:"Kaushan Script",cursive;font-size:44px;line-height:46px;color:var(--purple)}
.services{position:relative;height:103px;background:linear-gradient(#fff,#ececec);border-top:1px solid var(--line);border-bottom:1px solid var(--line)}
.services ul{position:absolute;left:184px;top:-1px;display:flex;list-style:none}
.services li{width:208px;height:104px;border-right:1px solid var(--line);text-align:center;padding-top:18px;color:var(--purple);font-size:17px}
.services li svg{display:block;margin:0 auto 10px}
.services li.active{background:var(--purple);color:#fff;border-color:var(--purple)}
.main{position:relative;height:545px;background:linear-gradient(#fff 0%,#ececee 45%,var(--grey-bg) 100%)}
.video{position:absolute;left:183px;top:35px;width:417px;height:248px;border:2px solid #e0e0e0;box-shadow:0 6px 8px -6px #999}
.video-still{width:100%;height:231px;background:linear-gradient(100deg,#9a8a80 0%,#cfd0cc 40%,#e6e6e4 100%)}
.video-bar{height:15px;background:#1c1c1c;position:relative}
.video-bar::before{content:"";position:absolute;left:0;top:0;width:45px;height:2px;background:#d22}
.intro{position:absolute;left:623px;top:42px;width:383px}
.intro h1{font-weight:400;font-size:27px;line-height:34px;color:var(--gold);letter-spacing:.8px}
.intro p{margin-top:15px;font-size:10.3px;line-height:16.5px;text-align:justify;letter-spacing:.2px}
.intro a{color:var(--purple);font-weight:700;text-decoration:none}
.cta{position:absolute;left:183px;top:313px;width:835px;height:64px;background:var(--purple);text-align:center;line-height:64px;font-size:21px;font-weight:300;color:var(--gold)}
.cta b{color:#fff;font-weight:700}
.cta .plain{color:#fff;font-weight:400}
.social{position:absolute;top:434px;left:0;width:1200px}
.social-item{position:absolute;display:flex;gap:12px}
.social-icon{width:54px;height:54px;border-radius:8px;background:linear-gradient(#fff,#e6e6e6);border:1px solid #ccc;box-shadow:0 4px 6px -3px #888;display:flex;align-items:center;justify-content:center}
.social-icon i{width:22px;height:22px;border-radius:4px;display:block}
.social h3{font-weight:400;font-size:14px;color:#222}
.social h3 em{font-style:normal;font-weight:700}
.social small{display:block;font-size:8.5px;color:#333}
.counts{display:flex;gap:10px;margin-top:8px;font-size:9px}
.counts span{border:1px solid #ccc;background:#fff;padding:3px 5px;color:var(--purple)}
.footer{position:absolute;top:1035px;left:0;width:1200px;height:133px;background:#fff;text-align:center}
.footer nav{margin-top:25px;font-size:11.5px;color:#444}
.footer nav span{margin:0 15px}
.footer p{margin-top:20px;font-size:9.5px;color:#666}
</style>
</head>
<body>
<div class="topbar"></div>
<header class="header">
  <div class="brand">Brindle</div>
  <nav class="nav">
    <a class="active" href="#">Home</a><span>⁝</span><a href="#">Investors</a><span>⁝</span><a href="#">Management</a><span>⁝</span><a href="#">Sellers</a><span>⁝</span><a href="#">Buyers</a><span>⁝</span><a href="#">Contact us</a>
  </nav>
  <div class="phone"><svg width="9" height="11" viewBox="0 0 9 11"><path d="M1 1h5l2 2v7H1z" fill="var(--purple)"/></svg>Call: (817) 555-0142 or (713) 555-0187</div>
</header>
<section class="hero">
  <div class="hero-photo" role="img" aria-label="Large brick family house with landscaped garden under a blue sky"></div>
  <div class="tagline">Committed to Success!</div>
</section>
<section class="services">
  <ul>
    <li class="active"><svg width="46" height="36" viewBox="0 0 46 36"><path d="M4 18 23 3l19 15M9 15v18h28V15" fill="none" stroke="#fff" stroke-width="3"/><rect x="18" y="21" width="10" height="12" fill="#fff"/></svg>Free Property Analysis</li>
    <li><svg width="46" height="36" viewBox="0 0 46 36"><path d="M3 18 23 2l20 16H37v16H9V18z" fill="var(--purple)"/><path d="M17 16l12 14M29 16 17 30" stroke="#fff" stroke-width="2.5"/></svg>In-House Maintenance</li>
    <li><svg width="46" height="36" viewBox="0 0 46 36"><rect x="4" y="2" width="38" height="24" fill="var(--purple)"/><rect x="8" y="6" width="30" height="16" fill="#fff"/><path d="M12 20v-6M16 20v-9M20 20v-4" stroke="var(--purple)" stroke-width="2.5"/><circle cx="30" cy="14" r="5" fill="var(--purple)"/><path d="M23 26v6M16 33h14" stroke="var(--purple)" stroke-width="2"/></svg>Interactive Online Portal</li>
    <li><svg width="46" height="36" viewBox="0 0 46 36"><path d="M2 18 13 8l11 10h-3v14H5V18z" fill="var(--purple)"/><circle cx="30" cy="18" r="8" fill="none" stroke="var(--purple)" stroke-width="3"/><path d="M36 24l7 7" stroke="var(--purple)" stroke-width="3"/></svg>Free MLS search</li>
  </ul>
</section>
<main class="main">
  <div class="video">
    <div class="video-still" role="img" aria-label="Welcome video from the company owner in the office"></div>
    <div class="video-bar"></div>
  </div>
  <div class="intro">
    <h1>Just a Better<br>Property Manager!</h1>
    <p>Brindle Homes and Leasing Inc. is a team of investors and real estate professionals that pride ourselves on helping fellow investors maximize the cash flow and performance of their real estate investments! We solve common problems from record keeping and headache tenants, to maintenance nightmares and much more!</p>
    <p>Click <a href="#">HERE</a> to get more information on investment opportunities!</p>
  </div>
  <div class="cta">Maximize Your Cash Flow! Click <b>HERE</b> <span class="plain">for a</span> <b>FREE</b> Property Analysis!</div>
  <div class="social">
    <div class="social-item" style="left:251px">
      <div class="social-icon"><i style="background:#3b5b9a"></i></div>
      <div><h3>We're on <em style="color:#2a5a9a">Friendbook</em></h3><small>Like us to see our daily updates!</small><div class="counts"><span>Like</span><span>20</span></div></div>
    </div>
    <div class="social-item" style="left:506px">
      <div class="social-icon"><i style="background:#5bb7e5"></i></div>
      <div><h3>We're on <em style="color:#3aa5e0;font-weight:400">Chirper</em></h3><small>Like us to see our daily updates!</small><div class="counts"><span>Share</span><span>241</span></div></div>
    </div>
    <div class="social-item" style="left:755px">
      <div class="social-icon"><i style="background:#d21f1f"></i></div>
      <div style="padding-top:14px"><h3>We're on <em style="color:#e01b1b">ViewTube</em></h3><small>See our Videos Channel!</small></div>
    </div>
  </div>
</main>
<footer class="footer">
  <nav>Home<span>I</span>Investors<span>I</span>Management<span>I</span>Sellers<span>I</span>Buyers<span>I</span>Contact us</nav>
  <p>© 2014 Brindle Homes and Leasing. All rights reserved.</p>
</footer>
</body>
</html>
```